Harbour Pizza gazebo signage project.

We are looking for signage for our mobile pizzeria gazebo structure. We sell pizza from a woodfired oven, Neapolitan style. We have a KR campervan which we sell pizza from too, which is yellow and black, so we would like to stick with those colours. The signage needs to be 2, 305cm x 76cm one for the top, and one for the bottom. It needs to state clearly the product is pizza. It also needs to include our logo, our website and that we sell Neapolitan style woodfired pizza. Our website is harbourpizza.co.uk to get a feel of our brand. We also don't want photos of pizza on the design.

Colors
000000
fbed22

Requirements
Must have
• The colours yellow and black and our logo on the top banner. Our website and the pinlane, tallyo and snapmoor logos on the bottom banner.

```html
<!DOCTYPE html>
<html lang="en">
<head>
<meta charset="utf-8">
<title>Harbour Pizza – Gazebo Banners</title>
<link rel="stylesheet" href="https://fonts.googleapis.com/css2?family=Arimo:wght@400;700&family=Bebas+Neue&display=swap">
<style>
  :root {
    --sign-yellow: #fedc22;
    --sign-charcoal: #353334;
    --ink-dark: #333132;
    --label-pink: #e5197f;
    --sheet-white: #ffffff;
    --sheet-edge: #555555;
  }
  * { margin: 0; padding: 0; box-sizing: border-box; }
  html, body {
    width: 1200px;
    height: 657px;
    overflow: hidden;
    background: var(--sheet-white);
  }
  .sheet {
    position: relative;
    width: 1200px;
    height: 657px;
    border: 1px solid var(--sheet-edge);
    font-family: "Arimo", Arial, sans-serif;
  }
  .banner-label {
    position: absolute;
    left: 0;
    width: 100%;
    text-align: center;
    font-size: 18px;
    color: var(--label-pink);
  }
  .banner-label--top { top: 9px; }
  .banner-label--bottom { top: 628px; }

  .banner {
    position: absolute;
    left: 28px;
    width: 1143px;
    height: 285px;
    border: 1px solid var(--sheet-edge);
  }
  .banner--top {
    top: 36px;
    background: var(--sign-yellow);
  }
  .banner--bottom {
    top: 337px;
    background: var(--sign-charcoal);
  }

  .strapline {
    position: absolute;
    top: 121px;
    font-family: "Bebas Neue", "Oswald", sans-serif;
    font-size: 44px;
    line-height: 44px;
    letter-spacing: 1px;
    color: var(--ink-dark);
    white-space: nowrap;
  }
  .strapline--left { left: 160px; }
  .strapline--right { left: 698px; }

  .brand-mark {
    position: absolute;
    left: 460px;
    top: 36px;
    width: 218px;
    height: 218px;
  }

  .social-row {
    position: absolute;
    top: 35px;
    left: 0;
    width: 100%;
    display: flex;
    justify-content: center;
    gap: 35px;
  }
  .social-badge {
    width: 92px;
    height: 92px;
    border-radius: 50%;
    background: var(--sign-yellow);
    color: var(--ink-dark);
    display: flex;
    align-items: center;
    justify-content: center;
    font-weight: 700;
    font-size: 15px;
  }

  .web-address {
    position: absolute;
    top: 144px;
    left: 0;
    width: 100%;
    text-align: center;
    font-weight: 700;
    font-size: 60px;
    line-height: 70px;
    color: var(--sheet-white);
  }
  .tagline {
    position: absolute;
    top: 222px;
    left: 0;
    width: 100%;
    text-align: center;
    font-weight: 700;
    font-size: 32px;
    line-height: 40px;
    color: var(--sign-yellow);
  }
</style>
</head>
<body>
  <div class="sheet">
    <p class="banner-label banner-label--top">Top Banner</p>

    <section class="banner banner--top">
      <p class="strapline strapline--left">Neapolitan Style</p>

      <svg class="brand-mark" viewBox="0 0 218 218" aria-label="Harbour Pizza">
        <circle cx="109" cy="109" r="100" fill="none" stroke="var(--ink-dark)" stroke-width="12"/>
        <text x="109" y="104" text-anchor="middle" font-family="Bebas Neue, Oswald, sans-serif" font-size="44" letter-spacing="2" fill="var(--ink-dark)">HARBOUR</text>
        <text x="109" y="148" text-anchor="middle" font-family="Bebas Neue, Oswald, sans-serif" font-size="44" letter-spacing="2" fill="var(--ink-dark)">PIZZA</text>
      </svg>

      <p class="strapline strapline--right">Woodfired Pizza</p>
    </section>

    <section class="banner banner--bottom">
      <div class="social-row">
        <span class="social-badge">pinlane</span>
        <span class="social-badge">snapmoor</span>
        <span class="social-badge">tallyo</span>
      </div>
      <p class="web-address">harbourpizza.co.uk</p>
      <p class="tagline">Catering for Weddings Events and Festivals</p>
    </section>

    <p class="banner-label banner-label--bottom">Bottom Banner</p>
  </div>
</body>
</html>
```